My website design

It Will be a to-go website for all service requests from the comfort of your home. services ranging from renting an electrician to fix your home electrical issues, DJ for your party, mark-up artist for your wedding and so on. Here are a few websites for inspiration:

https://www.dwellnook.example/
https://www.chorefinch.example/
https://www.pinlatch.example/

Number of Pages Required

5+ page

Requirements
Must have
• User's registration form
pros resgistation form
filling out job request form
quotes sent sent back to job requester from various pros within the same zip code
quote accepted
ability to review pros once jobs are completed

```html
<!DOCTYPE html>
<html lang="en">
<head>
<meta charset="utf-8">
<title>Fixora – Log in</title>
<link rel="stylesheet" href="https://fonts.googleapis.com/css2?family=Poppins:wght@400;500;600&display=swap">
<style>
  :root {
    --green: #3bb54a;
    --white: #ffffff;
    --ink: #111111;
    --text: #222222;
    --muted: #666666;
    --border: #c9c9c9;
    --rule: #d6d6d6;
    --social-blue: #3a589b;
    --social-red: #d93b31;
    --bg-top: #6b7884;
    --bg-mid: #596674;
    --bg-bottom: #4a5664;
  }
  * { box-sizing: border-box; margin: 0; padding: 0; }
  html, body { width: 1200px; height: 588px; overflow: hidden; }
  body { font-family: "Poppins", sans-serif; position: relative; color: var(--text); }

  .hero-photo {
    position: absolute; inset: 0;
    background: radial-gradient(ellipse at 50% 40%, var(--bg-top) 0%, var(--bg-mid) 55%, var(--bg-bottom) 100%);
  }

  .brand {
    position: absolute; left: 86px; top: 28px;
    display: flex; align-items: center; gap: 10px;
  }
  .brand-mark { width: 34px; height: 34px; background: var(--green); }
  .brand-name {
    font-size: 24px; font-weight: 500; color: var(--white);
    letter-spacing: 9px;
  }

  .site-nav {
    position: absolute; top: 31px; left: 784px;
    display: flex; align-items: center;
  }
  .btn-join {
    width: 125px; height: 38px; background: var(--green); color: var(--white);
    font-size: 12px; font-weight: 600; display: flex; align-items: center; justify-content: center;
    text-decoration: none;
  }
  .nav-link {
    color: var(--white); font-size: 12px; font-weight: 500; text-decoration: none;
  }
  .nav-explore { margin-left: 33px; }
  .nav-signup { margin-left: 30px; }
  .nav-login { margin-left: 27px; }

  .login-card {
    position: absolute; left: 434px; top: 109px; width: 332px; height: 431px;
    background: var(--white); border-radius: 4px;
  }
  .login-title {
    position: absolute; top: 24px; width: 100%; text-align: center;
    font-size: 25px; font-weight: 500; color: var(--ink);
  }
  .field-label {
    position: absolute; left: 25px; font-size: 11.5px; color: var(--ink);
  }
  .label-email { top: 75px; }
  .label-password { top: 161px; }
  .field-input {
    position: absolute; left: 25px; width: 283px; height: 45px;
    border: 1px solid var(--border); border-radius: 2px;
    display: flex; align-items: center; padding: 0 17px;
    font-size: 11.5px; color: var(--muted);
  }
  .input-email { top: 102px; }
  .input-password { top: 187px; justify-content: space-between; font-size: 10px; letter-spacing: 1px; }
  .eye-icon { width: 14px; height: 10px; }

  .options-row {
    position: absolute; left: 25px; top: 243px; width: 283px;
    display: flex; justify-content: space-between; align-items: center;
    font-size: 9px;
  }
  .keep-logged { display: flex; align-items: center; gap: 5px; color: #444; }
  .checkbox { width: 10px; height: 10px; border: 1px solid #777; border-radius: 2px; }
  .forgot-link { color: var(--green); text-decoration: none; }

  .btn-login {
    position: absolute; left: 25px; top: 275px; width: 283px; height: 44px;
    background: var(--green); color: var(--white); font-size: 14px;
    display: flex; align-items: center; justify-content: center; border-radius: 2px;
  }
  .divider {
    position: absolute; left: 25px; top: 330px; width: 283px;
    display: flex; align-items: center; gap: 8px; color: #888; font-size: 13px;
  }
  .divider::before, .divider::after { content: ""; flex: 1; height: 1px; background: var(--rule); }

  .btn-social {
    position: absolute; top: 357px; width: 135px; height: 45px;
    color: var(--white); font-size: 14px; border-radius: 2px;
    display: flex; align-items: center; justify-content: center;
  }
  .btn-friendsphere { left: 25px; background: var(--social-blue); }
  .btn-searchly { left: 172px; background: var(--social-red); }
</style>
</head>
<body>
  <div class="hero-photo" role="img" aria-label="Background photo of a tradesperson wearing a tool belt, holding a drill and a coiled cable"></div>

  <header>
    <a class="brand" href="#">
      <span class="brand-mark"></span>
      <span class="brand-name">FIXORA</span>
    </a>
    <nav class="site-nav">
      <a class="btn-join" href="#">Join as a pro</a>
      <a class="nav-link nav-explore" href="#">Explore</a>
      <a class="nav-link nav-signup" href="#">Sign Up</a>
      <a class="nav-link nav-login" href="#">Log in</a>
    </nav>
  </header>

  <main class="login-card">
    <h1 class="login-title">Welcome back</h1>
    <div class="field-label label-email">Email Address</div>
    <div class="field-input input-email">demo@mailbox.example</div>
    <div class="field-label label-password">Password</div>
    <div class="field-input input-password">
      <span>*********</span>
      <svg class="eye-icon" viewBox="0 0 14 10" aria-hidden="true">
        <path d="M1 5 C4 0.5 10 0.5 13 5 C10 9.5 4 9.5 1 5 Z" fill="none" stroke="#999" stroke-width="1"/>
        <circle cx="7" cy="5" r="2" fill="#999"/>
      </svg>
    </div>
    <div class="options-row">
      <label class="keep-logged"><span class="checkbox"></span>Keep me logged in</label>
      <a class="forgot-link" href="#">Forgot Password</a>
    </div>
    <div class="btn-login">Log In</div>
    <div class="divider">or</div>
    <div class="btn-social btn-friendsphere">Friendsphere</div>
    <div class="btn-social btn-searchly">Searchly</div>
  </main>
</body>
</html>
```